Sunvale products by Dorvimal. Beauty, skin care cosmetic products

We are an all natural and organic beauty product company looking for a logo an label design ideas. Our motto is to make products that are safe, natural, in harmony with the earth and that really work. Our products will contribute to the transition from the Old Earth to the Sunvale (as the image of the two worlds suggests). The earths can be mixed in the label. The label example is a rough sketch.

The label needs to be 1 (one) inch high and 7 inch long.

Target Market(s)

Products made with natural and organic ingredients. Beauty and skin products

Requirements
Must have
• My project must be standing out. We want customers to be draw to he product on the shelf. Wow, this label is different? what is it? All natural? I must try it.
• Must be bold but not outrageous.
• The two earth can be placed on right and left side of the tree of life on the second attachment
Nice to have
• The two Earth can be in the back ground suggesting that this product takes us from chemically and artificially filled products to something new that is in harmony with nature and health.
Should not have
• Should not be boring. Ordinary, easy to forget and ignore patterns, lettering, logos.

```html
<!DOCTYPE html>
<html lang="en">
<head>
<meta charset="UTF-8">
<title>Sunvale Products – Under-Arm-Balm Label</title>
<link href="https://fonts.googleapis.com/css2?family=Roboto+Condensed:wght@300;400&family=Roboto:wght@700;900&family=Alegreya:wght@400;500&display=swap" rel="stylesheet">
<style>
  :root {
    --backdrop: #dcdcdc;
    --label-navy: #1c2a8c;
    --label-deep: #121c6a;
    --label-panel: #17227a;
    --name-band: #0f1760;
    --ink-white: #ffffff;
    --ink-soft: #e6e9f7;
    --earth-old: #6b5a2e;
    --earth-new: #2f62c8;
  }
  * { box-sizing: border-box; margin: 0; padding: 0; }
  html, body { width: 1200px; height: 1006px; overflow: hidden; }
  body {
    background: var(--backdrop);
    display: flex;
    align-items: center;
    justify-content: center;
  }
  .label {
    position: relative;
    width: 1120px;
    height: 400px;
    background:
      radial-gradient(circle at 62% 40%, #2434a0 0%, var(--label-navy) 45%, var(--label-deep) 100%);
    display: grid;
    grid-template-columns: 250px 72px 1fr 150px;
    overflow: hidden;
  }
  .stars { position: absolute; inset: 0; pointer-events: none; }
  .info-panel {
    position: relative;
    background: var(--label-panel);
    padding: 38px 22px 30px 28px;
    color: var(--ink-soft);
    font-family: 'Roboto Condensed', sans-serif;
    font-weight: 300;
    font-size: 16px;
    line-height: 1.35;
    display: flex;
    flex-direction: column;
    justify-content: space-between;
  }
  .info-panel h3 { font-weight: 400; font-size: 17px; margin-bottom: 4px; }
  .name-band {
    position: relative;
    background: var(--name-band);
    display: flex;
    align-items: center;
    justify-content: center;
  }
  .name-band span {
    transform: rotate(-90deg);
    white-space: nowrap;
    font-family: 'Roboto', sans-serif;
    font-weight: 900;
    font-size: 54px;
    letter-spacing: 2px;
    color: var(--ink-white);
  }
  .front {
    position: relative;
    display: flex;
    flex-direction: column;
    align-items: center;
    padding-top: 22px;
  }
  .two-earths {
    width: 380px;
    height: 175px;
    border-radius: 90px;
    background: linear-gradient(90deg, var(--earth-old) 0%, #4a4f3a 35%, #1e3c8a 60%, var(--earth-new) 100%);
  }
  .brand {
    margin-top: 16px;
    font-family: 'Alegreya', serif;
    font-weight: 500;
    font-size: 52px;
    color: var(--ink-white);
  }
  .product {
    margin-top: 6px;
    font-family: 'Roboto Condensed', sans-serif;
    font-weight: 300;
    font-size: 38px;
    color: var(--ink-white);
  }
  .claim {
    position: absolute;
    left: 0; right: -150px; bottom: 0;
    height: 50px;
    background: var(--label-deep);
    text-align: center;
    line-height: 50px;
    font-family: 'Roboto', sans-serif;
    font-weight: 700;
    font-size: 30px;
    color: var(--ink-white);
    padding-right: 150px;
  }
  .side {
    position: relative;
    display: flex;
    flex-direction: column;
    align-items: center;
    padding-top: 28px;
    font-family: 'Roboto Condensed', sans-serif;
    font-weight: 300;
    color: var(--ink-white);
    text-align: center;
  }
  .badge {
    width: 70px; height: 70px;
    border-radius: 50%;
    border: 2px solid var(--ink-white);
  }
  .free-of { margin-top: 10px; font-size: 20px; }
  .net-weight {
    margin-top: 70px;
    width: 140px;
    padding: 24px 0;
    background: var(--label-deep);
    font-size: 26px;
    line-height: 1.3;
  }
</style>
</head>
<body>
  <div class="label">
    <svg class="stars" viewBox="0 0 1120 400" aria-hidden="true">
      <g fill="#ffffff">
        <circle cx="360" cy="60" r="1.6" opacity=".7"/>
        <circle cx="420" cy="300" r="5" opacity=".6"/>
        <circle cx="890" cy="200" r="2" opacity=".7"/>
        <circle cx="930" cy="330" r="1.5" opacity=".6"/>
        <circle cx="500" cy="140" r="1.2" opacity=".5"/>
        <circle cx="760" cy="45" r="1.4" opacity=".6"/>
        <circle cx="1040" cy="120" r="1.2" opacity=".5"/>
        <circle cx="620" cy="320" r="1.6" opacity=".5"/>
        <circle cx="150" cy="250" r="1.2" opacity=".4"/>
        <circle cx="210" cy="90" r="1" opacity=".4"/>
      </g>
    </svg>

    <section class="info-panel">
      <div class="ingredients">
        <h3>Ingredients:</h3>
        <p>Organic Shea Butter, Arrowroot Powder, Kaolinite (Natural Clay).</p>
      </div>
      <div class="directions">
        <p>Apply a small amount of the product to clean underarms. After a shave it may tingle. Stop use if irritation occurs.</p>
      </div>
    </section>

    <div class="name-band"><span>DORVIMAL</span></div>

    <section class="front">
      <div class="two-earths" role="img" aria-label="Illustration of a cracked old earth joined to a bright blue new earth"></div>
      <div class="brand">Sunvale Products</div>
      <div class="product">Under - Arm-Balm</div>
      <div class="claim">100% Natural Ingredients</div>
    </section>

    <aside class="side">
      <div class="badge"></div>
      <div class="free-of">No Phthalates</div>
      <div class="net-weight">Net Wt. 2 oz<br>(56g)</div>
    </aside>
  </div>
</body>
</html>
```